We need to re-design our website www.crestlinetasks.com.

We are currently featuring one enterprise app that connects phone user's with Velnaro Workboard Central. We only have a version for Talvix Handset so far. But soon we will be lauching the versions for oBrick and Mervalo.

We need a design that is appealing to corporation users of Velnaro Workboard Central. We need a framework tat allow us to feature all the different versions of the app.

Target Market(s)

enterprise mobile user's of Workboard Central

Industry/Entity Type

Mervalo

Requirements
Must have
• * Link to our current blog: blog.crestlinetasks.com
* Link to Pellora, Vantuo and Corvexa

```html
<!DOCTYPE html>
<html lang="en">
<head>
<meta charset="utf-8">
<title>Workboard Central Mobile</title>
<link href="https://fonts.googleapis.com/css2?family=Arimo:wght@400;700&family=Raleway:wght@100;200&family=Comfortaa:wght@300;400&display=swap" rel="stylesheet">
<style>
:root{
  --ink:#1c1c1c;
  --muted:#8a8a8a;
  --blue:#2a78a6;
  --tab:#2a75a3;
  --band-top:#3a3a3a;
  --band-bottom:#5a5a5a;
  --rule:#dcdcdc;
  --icon:#b4b4b4;
  --mervalo:#8dbb2a;
  --obrick:#2d4e78;
  --talvix:#f2b90f;
  --badge-mervalo:#7ab51d;
  --badge-obrick:#1f4e8c;
  --badge-talvix:#e8a21a;
  --ribbon:#e0463c;
  --card:#efefef;
}
*{margin:0;padding:0;box-sizing:border-box}
html,body{width:1200px;height:800px;overflow:hidden;background:#fff}
body{font-family:"Arimo",Arial,sans-serif;color:var(--ink);position:relative}
.abs{position:absolute}
.hero{left:0;top:0;width:1200px;height:182px;background:linear-gradient(180deg,var(--band-top),var(--band-bottom))}
.hero-column{left:197px;top:0;width:50px;height:182px;background:rgba(255,255,255,.07)}
.hero-marker{left:216px;top:0;width:0;height:0;border-left:6px solid transparent;border-right:6px solid transparent;border-top:5px solid #fff}
.main-nav{left:207px;top:12px;display:flex;gap:0;font-size:11px;color:#fff}
.main-nav a{color:#fff;text-decoration:none;margin-right:24px}
.main-nav a:nth-child(2){margin-right:30px}
.platform-badges{left:710px;top:0;display:flex;gap:2px}
.platform-badge{width:95px;height:27px;color:#fff;font-size:10px;display:flex;align-items:center;justify-content:center;letter-spacing:.5px}
.platform-badge.mervalo{background:var(--badge-mervalo)}
.platform-badge.obrick{background:var(--badge-obrick)}
.platform-badge.talvix{background:var(--badge-talvix)}
.brand-title{left:206px;top:120px;font-family:"Raleway",sans-serif;font-weight:100;font-size:56px;line-height:66px;color:#fff;white-space:nowrap;letter-spacing:-1px}
.brand-title .soft{color:#8a8a8a}
.tagline{left:206px;top:181px;font-family:"Comfortaa",sans-serif;font-weight:300;font-size:17px;letter-spacing:2px;color:#333}
.os-filter{left:215px;top:251px;font-size:9px;color:#666;display:flex;align-items:center;gap:8px}
.os-filter .caret{border-left:4px solid transparent;border-right:4px solid transparent;border-top:4px solid #777;margin-top:2px}
.section-tabs{left:816px;top:244px;display:flex;font-size:10px}
.section-tabs a{color:#222;text-decoration:none;padding:0 11px;line-height:22px}
.section-tabs a.active{background:var(--tab);color:#fff;width:61px;text-align:center;margin-left:8px}
.news-list{left:196px;top:292px;width:420px}
.news-item{position:relative;border-bottom:1px solid var(--rule);padding-left:49px}
.news-item .icon{position:absolute;left:3px;top:4px}
.news-item h3{font-size:11px;font-weight:400;color:var(--blue);line-height:13px}
.news-item p{font-size:9px;line-height:12.5px;color:#111;width:350px}
.news-item .meta{position:absolute;right:0;bottom:1px;font-size:7.5px;color:var(--muted)}
.news-item .meta span{margin-left:16px}
.news-item.milestone h3{font-size:17px;line-height:20px}
.divider{left:645px;top:292px;width:1px;height:334px;background:#e2e2e2}
.versions-title{left:741px;top:290px;font-size:17px;color:var(--blue)}
.version-card{left:736px;width:229px;height:38px;background:var(--card);border-radius:4px;box-shadow:0 1px 3px rgba(0,0,0,.25);overflow:hidden}
.version-card .dot{position:absolute;left:5px;top:3px;width:32px;height:32px;border-radius:50%}
.version-card .name{position:absolute;left:46px;top:7px;font-size:12px;color:#222}
.version-card .date{position:absolute;left:46px;top:21px;font-size:8px;color:#666}
.version-card .num{position:absolute;right:12px;top:7px;font-size:21px;color:var(--blue)}
.ribbon{right:-14px;top:5px;width:50px;height:11px;background:var(--ribbon);color:#fff;font-size:6px;text-align:center;line-height:11px;transform:rotate(45deg)}
.footer-rule{left:181px;top:716px;width:838px;height:1px;background:#555}
.footer-download{left:196px;top:740px;font-size:11px;letter-spacing:.5px;color:#222}
.store-dot{top:730px;width:32px;height:32px;border-radius:50%;color:#fff;font-size:13px;display:flex;align-items:center;justify-content:center;text-decoration:none}
.footer-links{left:849px;top:741px;font-size:9px;display:flex;gap:16px}
.footer-links a{color:#222;text-decoration:none}
</style>
</head>
<body>
<div class="abs hero" role="img" aria-label="Dark woven texture header band"></div>
<div class="abs hero-column"></div>
<div class="abs hero-marker"></div>
<nav class="abs main-nav">
  <a href="#">HOME</a><a href="#">ABOUT</a><a href="#">CONTACT US</a><a href="#">FOLLOW US</a>
</nav>
<div class="abs platform-badges">
  <a class="platform-badge mervalo">MERVALO</a>
  <a class="platform-badge obrick">OBRICK</a>
  <a class="platform-badge talvix">TALVIX HANDSET 7</a>
</div>
<h1 class="abs brand-title">WORKBOARD CENTRAL <span class="soft">MOBILE</span></h1>
<p class="abs tagline">manage your server from everywhere, whenever you want</p>

<div class="abs os-filter">OS INDEPENDENT <span class="caret"></span></div>
<nav class="abs section-tabs">
  <a href="#">GALLERY</a><a href="#">SPECS</a><a class="active" href="#">NEWS</a>
</nav>

<div class="abs news-list">
  <div class="news-item" style="height:48px">
    <svg class="icon" width="32" height="32" viewBox="0 0 32 32"><circle cx="16" cy="16" r="15" fill="none" stroke="var(--icon)" stroke-width="2"/><circle cx="16" cy="16" r="7" fill="none" stroke="var(--icon)" stroke-width="4" stroke-dasharray="3 2.5"/><circle cx="16" cy="16" r="3" fill="var(--icon)"/></svg>
    <h3>OBRICK OS APP</h3>
    <p>Application for oBrick OS is ready to be downloaded from Brick Market OS 5 or greater is required.</p>
    <div class="meta">Oct, 2012<span>read more</span></div>
  </div>
  <div class="news-item" style="height:62px;padding-top:13px">
    <svg class="icon" style="top:18px" width="32" height="32" viewBox="0 0 32 32"><circle cx="16" cy="16" r="15" fill="none" stroke="var(--icon)" stroke-width="2"/><circle cx="16" cy="16" r="7" fill="none" stroke="var(--icon)" stroke-width="4" stroke-dasharray="3 2.5"/><circle cx="16" cy="16" r="3" fill="var(--icon)"/></svg>
    <h3>MERVALO APP</h3>
    <p>Mervalo version (alfa 1.0) of the app is ready and it can be downloaded from Mervalo Shelf.</p>
    <div class="meta">Oct, 2012<span>read more</span></div>
  </div>
  <div class="news-item milestone" style="height:62px;padding-top:25px">
    <svg class="icon" style="top:18px" width="34" height="30" viewBox="0 0 34 30"><polyline points="3,27 11,14 19,19 31,3" fill="none" stroke="var(--icon)" stroke-width="2"/><circle cx="3" cy="27" r="2" fill="var(--icon)"/><circle cx="11" cy="14" r="2" fill="var(--icon)"/><circle cx="19" cy="19" r="2" fill="var(--icon)"/><circle cx="31" cy="3" r="2" fill="var(--icon)"/></svg>
    <h3>OVER 1.000 UNIQUE DOWNLOADS</h3>
  </div>
  <div class="news-item" style="height:63px;padding-top:15px">
    <svg class="icon" style="top:22px" width="30" height="28" viewBox="0 0 30 28"><path d="M2 2h26v17H11l-6 6v-6H2z" fill="var(--icon)"/><path d="M6 7h18M6 11h18M6 15h18" stroke="#fff" stroke-width="1.5"/></svg>
    <h3>WORKBOARD CENTRAL HAS A NEW WEB-PAGE</h3>
    <p>We are happy to announce that Workboard Central got new looks. Any comments and suggestions are more than welcome on our mail.</p>
    <div class="meta">Sep, 2012<span>read more</span></div>
  </div>
  <div class="news-item" style="height:64px;padding-top:16px">
    <svg class="icon" style="top:20px" width="30" height="32" viewBox="0 0 30 32"><path d="M15 2v20M7 14l8 8 8-8" fill="none" stroke="var(--icon)" stroke-width="3"/><path d="M4 29h22" stroke="var(--icon)" stroke-width="3"/></svg>
    <h3>UPDATE - TALVIX HANDSET 7</h3>
    <p>A new, updated version for Talvix Handset 7 platform; v1.4</p>
    <div class="meta">Sep, 2012<span>read more</span></div>
  </div>
</div>

<div class="abs divider"></div>

<h2 class="abs versions-title" style="font-weight:400">LATEST VERSIONS</h2>
<div class="abs version-card" style="top:335px">
  <span class="dot" style="background:var(--mervalo)"></span>
  <span class="name">MERVALO</span><span class="date">release date: 3.9.2012</span><span class="num">v1.2</span>
</div>
<div class="abs version-card" style="top:385px">
  <span class="dot" style="background:var(--obrick)"></span>
  <span class="name">OBRICK OS</span><span class="date">release date: 16.9.2012</span><span class="num">v1.2</span>
</div>
<div class="abs version-card" style="top:434px">
  <span class="dot" style="background:var(--talvix)"></span>
  <span class="name">TALVIX HANDSET 7</span><span class="date">release date: 1.9.2012</span><span class="num">v1.4</span>
  <span class="abs ribbon">NEW</span>
</div>

<div class="abs footer-rule"></div>
<div class="abs footer-download">DOWNLOAD</div>
<a class="abs store-dot" style="left:300px;background:var(--mervalo)" aria-label="Mervalo">M</a>
<a class="abs store-dot" style="left:350px;background:var(--obrick)" aria-label="oBrick">O</a>
<a class="abs store-dot" style="left:401px;background:var(--talvix)" aria-label="Talvix Handset">T</a>
<nav class="abs footer-links"><a href="#">Help</a><a href="#">Terms and Conditions</a></nav>
</body>
</html>
```